Skin Care business card for esthetician that is home based

I need a business card for my esthetician business. I would like to use a picture provided.
I want the picture #1 that I have provided to be as the main background with my title and the moto underneath in smaller lettering. Below that as a seperate thing I would like my full name and underneath in small letters to say "esthetician".
As a seperate paragraph I would like my address then phone number, email and my website that I have provided in the business card details.
On the back side I would like my second picture to be small and in the top left corner and then have the "nice to haves" details to be at the center bottom of the card.
Target Market(s)
mosty women between 18 and 60 years old
Industry/Entity Type
Skin Care
Contact Information for Business Card
Velvet Bloom Skin Care - Main Title
Your glow, gently restored! - motto
Marisol Teodora Vinchek -
Phone: 314.827.5093
7382 SW 9th Avenue
Oakvale WA 98472
oakvaleskincare@mailhaven.example
www.oakvaleskincare.example
Must have
- Picure I provided or other similar photo.
Nice to have
- On the back side:
Your glow, gently restored!
www.oakvaleskincare.example

```html
<!DOCTYPE html>
<html lang="en">
<head>
<meta charset="utf-8">
<title>Velvet Bloom Skin Care – Business Card</title>
<link rel="stylesheet" href="https://fonts.googleapis.com/css2?family=Montserrat:wght@500;600&display=swap">
<style>
  :root {
    --backdrop: #b9b9b9;
    --card-dark: #2e2c2c;
    --card-back: #353434;
    --photo-deep: #3a2c25;
    --photo-warm: #6b5243;
    --portrait-light: #cfc6bb;
    --portrait-mid: #8f8378;
    --gold: #d2ad5c;
    --gold-line: #c49a45;
    --ink-light: #f2efe9;
  }
  * { box-sizing: border-box; margin: 0; padding: 0; }
  html, body { width: 1200px; height: 675px; overflow: hidden; }
  body {
    background: var(--backdrop);
    font-family: "Montserrat", sans-serif;
    position: relative;
  }
  .card {
    position: absolute;
    top: 189px;
    width: 520px;
    height: 297px;
    border-radius: 14px;
    overflow: hidden;
  }
  /* Front */
  .card-front { left: 50px; background: var(--card-dark); }
  .front-photo {
    position: absolute; inset: 0;
    background: radial-gradient(ellipse at 38% 40%, var(--photo-warm) 0%, var(--photo-deep) 55%, var(--card-dark) 100%);
    opacity: .85;
  }
  .front-content { position: absolute; inset: 0; }
  .brand-name {
    position: absolute; top: 30px; left: 0; right: 0;
    text-align: center;
    color: var(--gold);
    font-weight: 500;
    font-size: 28px;
    line-height: 34px;
    letter-spacing: .5px;
  }
  .rule { position: absolute; height: 1.5px; background: var(--gold-line); }
  .rule-top { top: 70px; left: 40px; right: 30px; }
  .front-content .motto {
    position: absolute; top: 77px; right: 70px;
    color: var(--gold); font-weight: 600; font-size: 10.5px; line-height: 14px;
    letter-spacing: 1.2px; text-transform: uppercase;
  }
  .person-name {
    position: absolute; top: 110px; left: 96px;
    color: var(--gold); font-weight: 600; font-size: 17px; line-height: 22px; letter-spacing: .3px;
  }
  .person-role {
    position: absolute; top: 134px; right: 88px;
    color: var(--ink-light); font-weight: 500; font-size: 11px; line-height: 14px;
  }
  .contact-list { position: absolute; top: 158px; left: 80px; list-style: none; }
  .contact-list li {
    display: flex; align-items: flex-start; gap: 10px;
    color: var(--ink-light); font-weight: 500; font-size: 13.5px; line-height: 19px;
  }
  .contact-list .icon { width: 12px; height: 12px; margin-top: 3px; flex: none; }
  .rule-bottom { top: 250px; left: 0; right: 0; }
  /* Back */
  .card-back { left: 630px; background: var(--card-back); }
  .portrait {
    position: absolute; top: 0; left: 0; width: 200px; height: 110px;
    background: linear-gradient(160deg, var(--portrait-mid), var(--portrait-light) 55%, var(--card-back));
    border-bottom-right-radius: 6px;
  }
  .back-rule { top: 110px; left: 0; right: 0; }
  .back-brand {
    position: absolute; top: 132px; right: 34px;
    color: var(--gold); font-weight: 500; font-size: 26px; line-height: 32px;
  }
  .back-motto {
    position: absolute; top: 168px; right: 36px;
    color: var(--gold); font-weight: 600; font-size: 10px; line-height: 14px;
    letter-spacing: 1.2px; text-transform: uppercase;
  }
  .back-rule-lower { top: 196px; left: 150px; right: 0; }
  .back-web {
    position: absolute; top: 212px; left: 0; right: 0;
    color: var(--ink-light); font-weight: 500; font-size: 14px; line-height: 18px;
    display: flex; justify-content: center; align-items: center; gap: 8px;
  }
  .back-web .icon { width: 11px; height: 11px; }
</style>
</head>
<body>
  <section class="card card-front">
    <div class="front-photo" role="img" aria-label="Photo of a relaxed client receiving a facial treatment with spa stones"></div>
    <div class="front-content">
      <div class="brand-name">Velvet Bloom Skin Care</div>
      <div class="rule rule-top"></div>
      <div class="motto">Your glow, gently restored!</div>
      <div class="person-name">Marisol Teodora Vinchek</div>
      <div class="person-role">Esthetician</div>
      <ul class="contact-list">
        <li>
          <svg class="icon" viewBox="0 0 12 12"><path d="M6 0.5a4 4 0 0 1 4 4c0 3-4 7-4 7s-4-4-4-7a4 4 0 0 1 4-4z" fill="var(--gold)"/><circle cx="6" cy="4.5" r="1.5" fill="var(--card-dark)"/></svg>
          <span>7382 SW 9th Avenue<br>Oakvale WA 98472</span>
        </li>
        <li>
          <svg class="icon" viewBox="0 0 12 12"><path d="M2.5 1h2l1 3-1.5 1a7 7 0 0 0 3 3l1-1.5 3 1v2a1 1 0 0 1-1 1A10 10 0 0 1 1.5 2a1 1 0 0 1 1-1z" fill="var(--gold)"/></svg>
          <span>314.827.5093</span>
        </li>
        <li>
          <svg class="icon" viewBox="0 0 12 12"><rect x="0.5" y="2" width="11" height="8" rx="1" fill="var(--gold)"/><path d="M1 2.5l5 4 5-4" fill="none" stroke="var(--card-dark)" stroke-width="1"/></svg>
          <span>oakvaleskincare@mailhaven.example</span>
        </li>
      </ul>
      <div class="rule rule-bottom"></div>
    </div>
  </section>

  <section class="card card-back">
    <div class="portrait" role="img" aria-label="Portrait of the esthetician in a white uniform"></div>
    <div class="rule back-rule"></div>
    <div class="back-brand">Velvet Bloom Skin Care</div>
    <div class="back-motto">Your glow, gently restored!</div>
    <div class="rule back-rule-lower"></div>
    <div class="back-web">
      <svg class="icon" viewBox="0 0 12 12"><circle cx="6" cy="6" r="5.5" fill="var(--gold)"/><circle cx="6" cy="6" r="2" fill="var(--card-back)"/></svg>
      <span>www.oakvaleskincare.example</span>
    </div>
  </section>
</body>
</html>
```